Business Card Design 2018 Pinecrest Machining

Hello,

We need a business card design to reflect our new website we just had designed ( http://www.pinecrestmachining.example/)

We are a growing machine shop looking to grow our clientele and are hoping to update our current business card design to match our website and industry

The colours and design of our website should match to achieve what we are looking for.

I have attached a few images for reference as well as our logo and ISO 9000 needs to be apparent on the card as well

Please let me know what you have :)
Please copy melanie@pinecrestmachining.example on all communication regarding this project

Thanks !!!

Industry/Entity Type

Business

Contact Information for Business Card

Company Name, employee name and title and contact details

Colors
f78f20
ffffff
00a990

Requirements
Must have
• Our logo, Iso 9000 same colours as our website http://www.pinecrestmachining.example/

```html
<!DOCTYPE html>
<html lang="en">
<head>
<meta charset="utf-8">
<title>Pinecrest Machining – Business Card</title>
<link rel="stylesheet" href="https://fonts.googleapis.com/css2?family=Open+Sans:wght@300;400;600;700&display=swap">
<style>
  :root {
    --backdrop: #3b3431;
    --card: #141414;
    --white: #ffffff;
    --orange: #f78f20;
    --teal: #00a990;
    --grey: #8a8a8a;
    --divider: #6a6a6a;
  }
  * { margin: 0; padding: 0; box-sizing: border-box; }
  html, body {
    width: 1200px; height: 900px; overflow: hidden;
    background: var(--backdrop);
    font-family: "Open Sans", sans-serif;
    color: var(--white);
  }
  .stage { position: relative; width: 1200px; height: 900px; }
  .card {
    position: absolute; top: 300px;
    width: 525px; height: 300px;
    background: var(--card);
    box-shadow: 0 10px 30px rgba(0,0,0,.45);
    overflow: hidden;
  }
  .card--front { left: 50px; }
  .card--back { left: 625px; }

  /* front */
  .brand { position: absolute; left: 28px; top: 128px; width: 220px; }
  .brand__name {
    display: flex; align-items: center; gap: 8px;
    font-weight: 700; font-size: 19px; line-height: 1.1; color: var(--white);
    white-space: nowrap;
  }
  .brand__mark { width: 13px; height: 13px; background: var(--white); flex: none; }
  .brand__tagline { margin-top: 10px; font-size: 16px; color: var(--white); white-space: nowrap; }
  .divider {
    position: absolute; left: 252px; top: 40px; width: 1px; height: 220px;
    background: var(--divider);
  }
  .contact {
    position: absolute; left: 270px; top: 46px; width: 240px;
    font-size: 11.5px; line-height: 1.55; white-space: nowrap;
  }
  .contact__name { color: var(--teal); font-weight: 700; font-size: 15px; line-height: 1.2; }
  .contact__title { color: var(--orange); font-size: 12.5px; margin-bottom: 14px; }
  .contact__list { list-style: none; }
  .contact__item { display: flex; align-items: center; gap: 7px; }
  .contact__item svg { width: 10px; height: 10px; flex: none; fill: var(--teal); }
  .contact__address { margin-top: 14px; font-size: 12px; }

  /* back */
  .back { position: absolute; inset: 0; display: flex; flex-direction: column; align-items: center; padding-top: 52px; }
  .cert { display: flex; flex-direction: column; align-items: center; line-height: 1; }
  .cert__standard { font-size: 24px; font-weight: 300; letter-spacing: .5px; }
  .cert__standard strong { font-weight: 700; }
  .cert__label { margin-top: 3px; font-size: 8px; letter-spacing: 3px; font-weight: 400; }
  .back .brand__name { margin-top: 20px; font-size: 24px; }
  .back .brand__mark { width: 16px; height: 16px; }
  .services { margin-top: 12px; color: var(--orange); font-weight: 600; font-size: 15px; letter-spacing: .5px; }
  .social { margin-top: 10px; width: 16px; height: 16px; background: var(--grey); border-radius: 2px; }
  .rule { margin-top: 8px; width: 190px; height: 1px; background: var(--divider); }
</style>
</head>
<body>
<div class="stage">
  <section class="card card--front" aria-label="Business card front">
    <div class="brand">
      <div class="brand__name"><span class="brand__mark"></span>Pinecrest Machining</div>
      <div class="brand__tagline">Precision CNC Machining</div>
    </div>
    <div class="divider"></div>
    <div class="contact">
      <div class="contact__name">DANIEL HARLOW</div>
      <div class="contact__title">Managing Director</div>
      <ul class="contact__list">
        <li class="contact__item"><svg viewBox="0 0 12 12"><path d="M3 1l2 3-1.2 1.2a7 7 0 0 0 3 3L8 7l3 2-1 2C5 11 1 7 1 2z"/></svg>555 214 3070</li>
        <li class="contact__item"><svg viewBox="0 0 12 12"><rect x="1" y="4" width="10" height="7" rx="1"/><rect x="3" y="1" width="6" height="3"/></svg>555 388 6124</li>
        <li class="contact__item"><svg viewBox="0 0 12 12"><path d="M1 3h10v7H1z"/><path d="M1 3l5 4 5-4" fill="none" stroke="#141414" stroke-width="1"/></svg>info@pinecrestmachining.example</li>
        <li class="contact__item"><svg viewBox="0 0 12 12"><circle cx="6" cy="6" r="5"/></svg>www.pinecrestmachining.example</li>
      </ul>
      <div class="contact__address">4120 Birchwood Rd<br>Millbrook, ON, K0A 1B2</div>
    </div>
  </section>

  <section class="card card--back" aria-label="Business card back">
    <div class="back">
      <div class="cert">
        <div class="cert__standard">ISO<strong>9001</strong></div>
        <div class="cert__label">CERTIFIED</div>
      </div>
      <div class="brand__name"><span class="brand__mark"></span>Pinecrest Machining</div>
      <div class="services">TURN - MILL - THREAD</div>
      <div class="social" role="img" aria-label="Social profile link"></div>
      <div class="rule"></div>
    </div>
  </section>
</div>
</body>
</html>
```